Steelcrest Process Systems. Needs a Business Card Design

We need a business card design for an engineering company which supplies industrial components (pumps, compressors, mechanical seals) provides repairs and services for above mentioned equipments. We offer a uniqe engineering solutions which help our customers to increase the productivness of their manufacturings, and energy savings.

Target Market(s)

Chemical and energy plants, refineries. Food industry and private consumers in a less.

Industry/Entity Type

Business

Contact Information for Business Card

Stylish and sleek design oriented on industrial area.

Requirements
Should not have
• company name shortening

```html
<!DOCTYPE html>
<html lang="en">
<head>
<meta charset="utf-8">
<title>Steelcrest Process Systems – Business Card</title>
<link href="https://fonts.googleapis.com/css2?family=Ubuntu:wght@500;700&family=Lato:wght@400;700&display=swap" rel="stylesheet">
<style>
  :root {
    --stage: #2b2b2b;
    --navy: #1d3a8c;
    --navy-deep: #152c70;
    --brand-blue: #1f3f9a;
    --accent-red: #e0392b;
    --paper: #f6f6f6;
    --ink: #2f2f2f;
    --ink-soft: #555;
    --map-grey: #d9d9d9;
    --front-text: #dde3f1;
  }
  * { margin: 0; padding: 0; box-sizing: border-box; }
  html, body { width: 1200px; height: 873px; overflow: hidden; }
  body { background: var(--stage); position: relative; font-family: "Lato", sans-serif; }

  .card {
    position: absolute;
    width: 540px;
    height: 310px;
    border-radius: 3px;
    overflow: hidden;
    box-shadow: 0 18px 40px rgba(0,0,0,.45);
  }

  /* Front side */
  .card-front { left: 50px; top: 120px; background: var(--navy); }
  .front-pattern {
    position: absolute; inset: 0;
    background: linear-gradient(135deg, var(--navy) 0%, var(--navy-deep) 55%, var(--navy) 100%);
  }
  .front-name {
    position: absolute; left: 34px; bottom: 36px;
    font-family: "Ubuntu", sans-serif; font-weight: 700;
    font-size: 30px; color: var(--front-text); letter-spacing: .3px;
  }

  /* Back side */
  .card-back { left: 610px; top: 440px; background: var(--paper); }
  .back-map {
    position: absolute; left: 40px; top: 62px; width: 470px; height: 170px;
    background: radial-gradient(ellipse at center, var(--map-grey) 0%, rgba(217,217,217,.35) 60%, rgba(217,217,217,0) 100%);
    opacity: .7;
  }
  .brand { position: absolute; left: 40px; top: 34px; display: flex; align-items: center; gap: 14px; }
  .brand-dot { width: 40px; height: 40px; border-radius: 50%; background: var(--brand-blue); }
  .brand-name {
    font-family: "Ubuntu", sans-serif; font-weight: 700;
    font-size: 22px; color: var(--brand-blue);
  }
  .holder { position: absolute; right: 34px; top: 112px; text-align: right; }
  .holder-name { font-weight: 700; font-size: 17px; color: var(--ink); }
  .holder-role { font-size: 13px; color: var(--ink-soft); margin-top: 2px; }

  .icon-tab {
    position: absolute; left: 0; top: 168px; width: 42px; height: 118px;
    background: var(--navy); border-radius: 0 8px 8px 0;
    display: flex; flex-direction: column; justify-content: space-around; align-items: center;
    padding: 6px 0;
  }
  .icon-tab svg { width: 16px; height: 16px; fill: #fff; }
  .contact-list {
    position: absolute; left: 58px; top: 172px; list-style: none;
    font-size: 12.5px; font-weight: 700; color: var(--ink-soft);
  }
  .contact-list li { height: 28px; line-height: 28px; }

  .trim { position: absolute; left: 0; bottom: 0; width: 540px; height: 40px; }
</style>
</head>
<body>

  <section class="card card-front" aria-label="Business card front">
    <div class="front-pattern" role="img" aria-label="Faceted navy polygon texture"></div>
    <p class="front-name">Steelcrest Process Systems</p>
  </section>

  <section class="card card-back" aria-label="Business card back">
    <div class="back-map" role="img" aria-label="Dotted world map in light grey"></div>

    <div class="brand">
      <span class="brand-dot"></span>
      <span class="brand-name">Steelcrest Process Systems</span>
    </div>

    <div class="holder">
      <p class="holder-name">Rafael Ortiz</p>
      <p class="holder-role">Owner / Founder</p>
    </div>

    <div class="icon-tab">
      <svg viewBox="0 0 24 24" aria-hidden="true"><path d="M3 8c0-2 4-4 9-4s9 2 9 4v2h-5V8H8v2H3z M6 12h12l2 8H4z"/></svg>
      <svg viewBox="0 0 24 24" aria-hidden="true"><path d="M7 2h10a1 1 0 0 1 1 1v18a1 1 0 0 1-1 1H7a1 1 0 0 1-1-1V3a1 1 0 0 1 1-1zm1 3v13h8V5z"/></svg>
      <svg viewBox="0 0 24 24" aria-hidden="true"><path d="M2 5h20v14H2z M3 6l9 7 9-7" stroke="#1d3a8c" stroke-width="1.5"/></svg>
      <svg viewBox="0 0 24 24" aria-hidden="true"><path d="M12 2a7 7 0 0 1 7 7c0 5-7 13-7 13S5 14 5 9a7 7 0 0 1 7-7zm0 4a3 3 0 1 0 0 6 3 3 0 0 0 0-6z"/></svg>
    </div>

    <ul class="contact-list">
      <li>555-014-2200 EXT. 230</li>
      <li>555-017-3381</li>
      <li>rafael@steelcrestprocess.com</li>
      <li>118 Harlow St, Brookfield IL 60513, US</li>
    </ul>

    <svg class="trim" viewBox="0 0 540 40" preserveAspectRatio="none" aria-hidden="true">
      <path d="M0 28 L440 28 Q455 28 460 20 L540 20 L540 40 L0 40 Z" fill="var(--accent-red)"/>
      <path d="M470 20 Q478 4 500 4 L540 4 L540 20 Z" fill="var(--brand-blue)"/>
    </svg>
  </section>

</body>
</html>
```